Modernise Business Card

Our company has been operating for 10 years. With the start of the new decade we are looking to refresh our business card design. We manufacture a range of industrial product shipping to customers internationally. A copy of our current card, both sides, is attached. We are looking for a mature professional appearance.

```html
<!DOCTYPE html>
<html lang="en">
<head>
<meta charset="utf-8">
<title>Veltrix Business Card</title>
<link rel="stylesheet" href="https://fonts.googleapis.com/css2?family=Poppins:ital,wght@0,400;0,700;1,800&display=swap">
<style>
  :root {
    --backdrop: #2c2c2e;
    --card: #ffffff;
    --brand: #1aa9d8;
    --ink: #555659;
    --card-shadow: rgba(0,0,0,0.45);
  }
  html, body {
    margin: 0;
    padding: 0;
    width: 1200px;
    height: 960px;
    overflow: hidden;
    background: var(--backdrop);
    font-family: "Poppins", sans-serif;
  }
  .canvas {
    position: relative;
    width: 1200px;
    height: 960px;
  }
  .card {
    position: absolute;
    width: 580px;
    height: 332px;
    background: var(--card);
    box-shadow: 0 14px 30px var(--card-shadow);
    box-sizing: border-box;
  }
  .card--front {
    left: 540px;
    top: 80px;
    display: flex;
    align-items: center;
    justify-content: center;
  }
  .wordmark {
    display: flex;
    align-items: center;
    gap: 16px;
    color: var(--brand);
    font-weight: 700;
    font-size: 78px;
    letter-spacing: -1px;
    line-height: 1;
  }
  .wordmark__square {
    width: 34px;
    height: 34px;
    background: var(--brand);
  }
  .card--back {
    left: 80px;
    top: 540px;
    padding: 64px 40px 0 44px;
  }
  .holder-name {
    position: absolute;
    right: 40px;
    top: 58px;
    margin: 0;
    color: var(--brand);
    font-weight: 800;
    font-style: italic;
    font-size: 27px;
    letter-spacing: 0.5px;
    text-transform: uppercase;
  }
  .contact {
    margin: 52px 0 0;
    font-size: 14px;
    line-height: 19px;
    color: var(--ink);
    font-style: normal;
  }
  .contact__label {
    color: var(--brand);
  }
  .address {
    margin-top: 8px;
  }
  .product-line {
    margin: 12px 0 0;
    font-size: 14px;
    color: var(--ink);
  }
  .product-line__dot {
    color: var(--brand);
    padding: 0 4px;
  }
</style>
</head>
<body>
<main class="canvas">
  <section class="card card--front" aria-label="Card front">
    <div class="wordmark">
      <span class="wordmark__square"></span>
      <span class="wordmark__name">Veltrix</span>
    </div>
  </section>

  <section class="card card--back" aria-label="Card back">
    <h1 class="holder-name">Sam Harlow</h1>
    <address class="contact">
      <div><span class="contact__label">China :</span> +86 139 5520 0417</div>
      <div><span class="contact__label">Australia:</span> +61 412 307 881</div>
      <div>sharlow@veltrixfittings.com</div>
      <div>www.veltrixfittings.com</div>
      <div class="address">
        <div>1208-3, Lantern Building</div>
        <div>77 Qiaoshan Road</div>
        <div>Harbor District Donglin 300120 China</div>
      </div>
    </address>
    <p class="product-line">Hydraulic Adapters<span class="product-line__dot">•</span>Hose Fittings<span class="product-line__dot">•</span>Quick Couplings</p>
  </section>
</main>
</body>
</html>
```